Card Game Design - 5 Faces Only (Islamic Geometry Inspired)

The idea behind this project is to design a set a cards for a game. The game works as follows:

1 - Everyday you start with a deck of cards
2 - As the day progresses each card contains an action to perform
3 - If you perform that action, you move the card, face-up, to the pack of the deck
4 - If you do not perform that action, you flip the card over and place it at the back of the deck.
5 - At the end of the day, you review your deck.

The front of each card contains 3 major elements:

1 - Title
2 - Value - ie a number, score for completing the act
3 - An encouraging statement

The back of each card contains 3 elements:

1 - Title
2 - Value - ie a number, essentially a “minus” number
3 - A calligraphic symbol that will take-up of most of the card.

The back of the card is a simpler single design. The front of the card is slightly more complex. The front cards need to be of four types. The difference in types should preferably be in both color and design changes that indicate the four types.

Thus, the designer will be designing essentially 5 card faces. The back is the same for all designs, but the front four can either be variations in color / form or both.

The front facing cards are of the following types:

1 - Prayer - these are the cards that will reflect a prayer to be performed
2 - Day - these will be cards with actions to be performed on Monday, Thursday and Friday
3 - Awrād - activities that are to be performed on a daily basis
4 - Daily - activities that are to be performed on a daily basis

Overall Design Ethic

Modern board games have beautifully designed cards that are uniquely branded. The overall ethos of these cards are that they should reflect traditional Islamic art in nature. Think beautiful designed geometric patterns and calligraphy. If one can weave these design elements in a card face that is beautifully showcases the main elements - title, point and statement - that would be ideal.For this design project,

I am looking to get the 5 cards in PSDs ready for printing. I will add the front facing text and the text for the reverse except for the calligraphic panel that is linked below. Nevertheless, sample fonts and texts should be provided so that overall harmony with the design can be effectively assessed.

The calligraphic symbol for the back can be found here:

https://www.pelvarin-find.example/results?q=brush+script+panel&set=img&ref=A1b2C3d4E5f6G7h8

A circular version and square version that show in the display are very appealing. Other versions can be used if assessed to have a better fit for the design.

Alternatively, a calligraphic rendering of the phrase "Astaghfirullah" can also be used. Samples here:

https://www.pelvarin-find.example/results?q=ink+phrase+lettering&set=img&ref=H9i8J7k6L5m4N3o2

Sample Design Ethos

https://www.pelvarin-find.example/results?q=framed+panel&set=img&ref=P1q2R3s4T5u6V7w8

https://www.pelvarin-find.example/results?set=img&q=gilded+manuscript+borders&ref=X9y8Z7a6B5c4D3e2F1g0h9

https://www.pelvarin-find.example/results?set=img&q=ornate+tile+motifs&ref=J1k2L3m4N5o6P7q8R9s0#view=_

https://www.pelvarin-find.example/results?q=star+lattice+patterns&set=img&ref=T1u2V3w4X5y6Z7a8

Board Game Ethos

https://www.pelvarin-find.example/results?set=img&q=tabletop+card+layouts&ref=B1c2D3e4F5g6H7i8J9k0

Font styles to use
Serif
Sans Serif

Requirements
Must have
• Elegant, unified design.
• Must be aesthetically pleasing.
• Beautiful and vivid coloring without being gaudy.
Nice to have
• Meaningful symbolism.
• For example: Two small circles in each top corner of the card. One with a stylized representation of the Tolvenne and the other the Spire of the Keeper's hall in Madinah.
• See: https://www.quillmarsh-stock.example/browse/stone+cube+shrine?page=3&layout=vertical&licensed=true&filter=safe&origin=related_browse
• See: https://www.pelvarin-find.example/results?q=brenhollow+college&set=img&ref=Q1w2E3r4T5y6U7i8O9p0A1s2D3f4G5h6J7k8L9z0X1c2V3b4N5m6

```html
<!DOCTYPE html>
<html lang="en">
<head>
<meta charset="utf-8">
<title>Daily Activity – Card Front and Back</title>
<link rel="stylesheet" href="https://fonts.googleapis.com/css2?family=Cinzel:wght@400;500&family=Amiri:wght@400&display=swap">
<style>
  :root {
    --page: #ffffff;
    --ink: #1f1a15;
    --deep: #3d342b;
    --front-border: #5f5847;
    --front-ornament: #b3ad95;
    --front-band: #c4bca6;
    --front-edge: #4d4538;
    --title-panel: #eeeae6;
    --cream-mid: #faefd9;
    --cream-edge: #b9ad86;
    --back-border: #a9a17b;
    --back-ornament: #6e6a55;
    --back-frame: #c9c1a3;
    --lattice-light: #d8cdb2;
    --lattice-dark: #4a4034;
    --silver-hi: #f2f2f2;
    --silver-lo: #8e8e8e;
    --light-text: #f1ede7;
  }
  * { box-sizing: border-box; margin: 0; padding: 0; }
  html, body { width: 1200px; height: 753px; overflow: hidden; background: var(--page); }
  body { position: relative; font-family: "Cinzel", serif; color: var(--ink); }

  .card { position: absolute; top: 71px; width: 426px; height: 596px; overflow: hidden; }
  .card--front { left: 140px; }
  .card--back { left: 671px; }
  .abs { position: absolute; }

  /* ---------- front ---------- */
  .front-ornament {
    inset: 0;
    background:
      radial-gradient(circle at 10% 8%, var(--front-ornament) 0, transparent 22%),
      radial-gradient(circle at 90% 8%, var(--front-ornament) 0, transparent 22%),
      radial-gradient(circle at 10% 94%, var(--front-ornament) 0, transparent 22%),
      radial-gradient(circle at 90% 94%, var(--front-ornament) 0, transparent 22%),
      linear-gradient(90deg, #8a846e 0%, var(--front-border) 8%, var(--front-border) 92%, #8a846e 100%);
  }
  .front-frame {
    left: 26px; top: 120px; width: 378px; height: 444px;
    background: var(--front-band);
    border: 5px solid var(--front-edge);
  }
  .title-panel {
    left: 55px; top: 100px; width: 316px; height: 58px;
    background: var(--title-panel);
    display: flex; align-items: center; justify-content: center;
    font-size: 27px; font-weight: 400;
    border-bottom: 3px solid #8a8478;
  }
  .cream-panel {
    left: 55px; width: 316px;
    background: radial-gradient(ellipse at center, var(--cream-mid) 20%, #efe2c8 60%, var(--cream-edge) 100%);
    border: 3px solid #d6d6d6;
    border-left-color: #bfbfbf;
  }
  .panel-top { top: 163px; height: 134px; display: flex; align-items: center; justify-content: center; padding-bottom: 14px; font-size: 27px; }
  .panel-bottom { top: 322px; height: 208px; }
  .statement-label {
    left: 0; top: 16px; width: 116px; height: 28px;
    background: var(--title-panel);
    font-size: 16px; display: flex; align-items: center; justify-content: center;
  }
  .statement-text {
    left: 0; right: 0; top: 60px;
    text-align: center; font-size: 18.3px; line-height: 26px;
  }

  .seal {
    border-radius: 50%;
    background: var(--deep);
    border: 5px solid var(--silver-lo);
    box-shadow: 0 0 0 2px var(--silver-hi), inset 0 0 0 2px #5b5045;
    overflow: hidden;
  }
  .corner-left { left: 16px; top: 11px; width: 106px; height: 106px; }
  .corner-right { left: 308px; top: 9px; width: 106px; height: 106px; }
  .corner-art { position: absolute; inset: 0; background: linear-gradient(160deg, var(--deep) 45%, #d9d3cb 46%, #efebe7 100%); }
  .corner-right .corner-art { background: linear-gradient(180deg, var(--deep) 38%, #e9e4de 39%, #e9e4de 60%, var(--deep) 61%, #3a3129 100%); }

  .banner {
    height: 50px;
    background: var(--deep);
    border: 4px solid var(--silver-lo);
    box-shadow: 0 0 0 2px var(--silver-hi);
    border-radius: 25px;
    color: var(--light-text);
    display: flex; align-items: center; justify-content: center;
    font-size: 31px; font-weight: 400; white-space: nowrap;
  }
  .front-banner { left: 90px; top: 46px; width: 257px; }

  .value-badge {
    width: 80px; height: 80px;
    display: flex; align-items: center; justify-content: center;
    font-family: "Amiri", serif; font-size: 46px; color: var(--light-text); line-height: 1;
  }
  .front-value { left: 173px; top: 271px; }

  /* ---------- back ---------- */
  .back-ornament {
    inset: 0;
    background:
      radial-gradient(circle at 8% 6%, var(--back-ornament) 0, transparent 18%),
      radial-gradient(circle at 92% 6%, var(--back-ornament) 0, transparent 18%),
      radial-gradient(circle at 8% 95%, var(--back-ornament) 0, transparent 18%),
      radial-gradient(circle at 92% 95%, var(--back-ornament) 0, transparent 18%),
      var(--back-border);
  }
  .back-frame { left: 26px; top: 26px; width: 385px; height: 550px; background: var(--back-frame); }
  .back-lattice {
    left: 33px; top: 33px; width: 371px; height: 536px;
    border: 3px solid var(--lattice-dark);
    background:
      radial-gradient(circle at 25% 15%, var(--lattice-light) 0, transparent 22%),
      radial-gradient(circle at 75% 15%, #a89a75 0, transparent 22%),
      radial-gradient(circle at 25% 85%, #9d9068 0, transparent 22%),
      radial-gradient(circle at 75% 85%, var(--lattice-light) 0, transparent 22%),
      linear-gradient(90deg, var(--lattice-dark) 0%, #8c8062 20%, #b7aa88 50%, #8c8062 80%, var(--lattice-dark) 100%);
  }
  .back-banner { left: 99px; top: 29px; width: 254px; height: 49px; }
  .medallion {
    left: 38px; top: 121px; width: 360px; height: 360px;
    border-radius: 50%;
    border: 6px solid #b8b098;
    background: radial-gradient(circle,
      #4a4036 0, #6a6055 14%, #3d342b 18%, #5c5247 26%, #3d342b 34%,
      #62584c 48%, #3d342b 60%, #574d42 78%, #3d342b 100%);
  }
  .medallion-ring { border-radius: 50%; border: 2px solid #e9e4de; left: 50%; top: 50%; transform: translate(-50%, -50%); }
  .ring-inner { width: 125px; height: 125px; }
  .ring-mid { width: 185px; height: 185px; border-width: 1.5px; }
  .back-value { left: 179px; top: 511px; }
</style>
</head>
<body>

  <section class="card card--front" aria-label="Daily activity card, front">
    <div class="abs front-ornament" role="img" aria-label="Floral arabesque border ornament"></div>
    <div class="abs front-frame"></div>

    <div class="abs title-panel">Asr - Fard</div>
    <div class="abs cream-panel panel-top">Lafaz In Arab</div>
    <div class="abs cream-panel panel-bottom">
      <div class="abs statement-label">Statement:</div>
      <p class="abs statement-text">In Arabic - Whomsoever<br>prays the bardayn<br>(Fajr &amp; Asr) enters Paradise.</p>
    </div>

    <div class="abs seal corner-left"><div class="corner-art" role="img" aria-label="Silhouette of the Spire of the Keeper's hall"></div></div>
    <div class="abs seal corner-right"><div class="corner-art" role="img" aria-label="Stylized Tolvenne shrine"></div></div>
    <h1 class="abs banner front-banner">Daily Activity</h1>

    <div class="abs seal value-badge front-value">٦</div>
  </section>

  <section class="card card--back" aria-label="Daily activity card, back">
    <div class="abs back-ornament" role="img" aria-label="Floral arabesque border ornament"></div>
    <div class="abs back-frame"></div>
    <div class="abs back-lattice" role="img" aria-label="Interlaced eight-pointed star geometric lattice"></div>
    <div class="abs medallion" role="img" aria-label="Circular calligraphy medallion">
      <div class="abs medallion-ring ring-mid"></div>
      <div class="abs medallion-ring ring-inner"></div>
    </div>
    <h2 class="abs banner back-banner">Daily Activity</h2>
    <div class="abs seal value-badge back-value">-٦</div>
  </section>

</body>
</html>
```